A Gallery type Web design

We are developing a Wordpress based website for a client that does design construction projects. E.g. Pools, Lobbies, Toilets, etc. The website will mainly be to showcase their past projects and the collections they have.
No programming required, we just need the designs!
A sample of what the client is looking for:
http://velmora.it/
Pages to include:
• Home – A nice slider design to showcase selected photos
• Main Category Template
• Sub Category Template
• About us
• Contact us
Example of their Main Categories and their Sub Categories:
Collections - Granite
- Marble
- Sculpture
Projects - Private
- Public
- Commercial
- Overseas
Installation - Vanity tops
- Hall areas
- Toilets
The Main Category is to show a sample and link the user to the respective Sub Categories. The Sub Categories are to showcase all the photos they have from the category. Please leave a little space to add some text or caption for the photo.
Designs need to be mobile responsive!
I've attached their logo and some sample photos to use for mock ups. Let me know if you have any questions!

```html
<!DOCTYPE html>
<html lang="en">
<head>
<meta charset="utf-8">
<title>Rockhaven — Home</title>
<link href="https://fonts.googleapis.com/css2?family=Fira+Sans+Condensed:wght@300;400;500&family=Raleway:wght@300;400&display=swap" rel="stylesheet">
<style>
:root{
  --red:#e0191f;
  --ink:#1b1b1b;
  --text:#6c6c6c;
  --light:#f2f2f2;
  --header:rgba(20,20,20,.82);
  --footer:#000;
  --footer-base:#1c1c1c;
  --rule:#dedede;
}
*{margin:0;padding:0;box-sizing:border-box}
html,body{width:736px;height:1200px;overflow:hidden;background:#fff}
body{position:relative;font-family:"Fira Sans Condensed",sans-serif;color:var(--ink)}
a{color:inherit;text-decoration:none}

.hero{position:absolute;left:0;top:0;width:736px;height:456px;
  background:radial-gradient(ellipse at 60% 35%,#8a8078 0%,#564e48 40%,#2a2624 75%,#151312 100%)}
.hero-shade{position:absolute;inset:0;background:linear-gradient(180deg,rgba(0,0,0,.15),rgba(0,0,0,.05) 60%,rgba(0,0,0,.3))}
.hero-title{position:absolute;left:0;right:0;top:238px;text-align:center;font-family:"Raleway",sans-serif;font-weight:300;
  font-size:36px;line-height:45px;color:#fff;letter-spacing:.5px}
.hero-sub{position:absolute;left:0;right:0;top:340px;text-align:center;font-family:"Raleway",sans-serif;font-size:10.5px;color:#fff;letter-spacing:.3px}
.slider-bars{position:absolute;left:288px;top:420px;display:flex;gap:6px}
.slider-bars span{width:30px;height:2px;background:rgba(255,255,255,.22)}
.slider-bars span.active{background:#fff}

.topbar{position:absolute;left:0;top:0;width:736px;height:40px;background:var(--header)}
.brand{position:absolute;left:28px;top:0;width:128px;height:64px;background:#cfcfcf;display:flex;align-items:center;justify-content:center;gap:6px}
.brand-mark{width:10px;height:10px;background:var(--red)}
.brand-name{font-size:17px;font-weight:500;color:var(--red);letter-spacing:.5px}
.nav{position:absolute;top:16px;left:0;font-size:9px;color:#fff;text-transform:uppercase}
.nav a{position:absolute;white-space:nowrap}
.nav a.current{color:var(--red)}
.dropdown{position:absolute;left:214px;top:40px;width:50px;height:52px;background:var(--red);padding:6px 0 0 7px;font-size:7.5px;line-height:14px;color:#fff}
.dropdown .muted{color:#5a0508}
.search{position:absolute;left:590px;top:14px;width:116px;height:17px;background:#4a4a4a;color:#aaa;font-size:7.5px;padding:4px 6px}
.search svg{position:absolute;right:4px;top:4px}

.hero-shadow{position:absolute;left:80px;top:456px;width:576px;height:26px;
  background:radial-gradient(ellipse 50% 100% at 50% 0%,rgba(0,0,0,.16),rgba(0,0,0,0) 100%)}

.tiles{position:absolute;left:28px;top:502px;width:679px;height:143px;display:flex;gap:1px}
.tile{position:relative;flex:1}
.tile-granite{background:linear-gradient(135deg,#8e8e8e,#5e5e5e 60%,#3e3e3e)}
.tile-marble{background:linear-gradient(135deg,#8d6a6a,#b89a98 50%,#6d4a47)}
.tile-sculpture{background:linear-gradient(135deg,#9c8883,#6b5a58 50%,#a8928b)}
.tile-label{position:absolute;left:23px;top:109px;font-size:19px;font-weight:300;color:#fff}
.tile svg{position:absolute;right:22px;top:110px}

.welcome{position:absolute;left:0;right:0;top:703px;text-align:center}
.section-title{font-size:16px;font-weight:300;color:var(--red);text-transform:uppercase}
.welcome p{width:545px;margin:20px auto 0;font-size:9.6px;line-height:16px;color:var(--text);font-weight:300}
.rule{position:absolute;left:28px;top:817px;width:679px;height:1px;background:var(--rule)}

.projects{position:absolute;left:0;right:0;top:845px;text-align:center}
.project-row{position:absolute;left:28px;top:888px;display:flex;gap:12px}
.project{width:126px}
.project-img{height:69px}
.project h3{margin-top:12px;font-size:10.5px;font-weight:400;color:#111}
.project p{margin-top:3px;font-size:6.5px;color:#888;text-transform:uppercase}
.dots{position:absolute;left:331px;top:1019px;display:flex;gap:7px}
.dots span{width:5px;height:5px;border-radius:50%;background:#999}
.dots span.active{background:#111}

.footer{position:absolute;left:0;top:1050px;width:736px;height:112px;background:var(--footer);color:#fff;text-align:center}
.social{position:absolute;left:330px;top:31px;display:flex;gap:8px}
.social span{width:13px;height:13px;border:1px solid #fff;border-radius:50%}
.footer-nav{position:absolute;left:0;right:0;top:66px;font-size:8.4px;font-weight:300;text-transform:uppercase;word-spacing:0}
.footer-nav a{margin:0 7px}
.legal{position:absolute;left:0;right:0;top:89px;font-size:8px;font-weight:300;text-transform:uppercase}
.base{position:absolute;left:0;top:1162px;width:736px;height:38px;background:var(--footer-base);color:#aaa;font-size:6.5px;text-align:center;padding-top:13px;text-transform:uppercase}
</style>
</head>
<body>

<section class="hero" role="img" aria-label="Photo of an elegant dining room and hallway with patterned chairs, table lamp and mosaic floor">
  <div class="hero-shade"></div>
</section>
<h1 class="hero-title">BRING A TOUCH<br>OF NATURE HOME!</h1>
<p class="hero-sub">LOREM IPSUM DOLOR SIT AMET CONSECTETUER ADIPISCI</p>
<div class="slider-bars"><span class="active"></span><span></span><span></span><span></span><span></span></div>

<header class="topbar">
  <a class="brand" href="#"><span class="brand-mark"></span><span class="brand-name">ROCKHAVEN</span></a>
  <nav class="nav">
    <a style="left:180px" href="#">Home</a>
    <a class="current" style="left:216px" href="#">Collections</a>
    <a style="left:276px" href="#">Projects</a>
    <a style="left:322px" href="#">Installations</a>
    <a style="left:386px" href="#">About us</a>
    <a style="left:434px" href="#">Contact us</a>
  </nav>
  <div class="search">SEARCH
    <svg width="8" height="8" viewBox="0 0 8 8"><circle cx="3.2" cy="3.2" r="2.4" fill="none" stroke="#999" stroke-width="1"/><line x1="5" y1="5" x2="7.5" y2="7.5" stroke="#999" stroke-width="1.2"/></svg>
  </div>
</header>
<div class="dropdown">GRANITE<br><span class="muted">MARBLE</span><br>SCULPTURE</div>

<div class="hero-shadow"></div>

<section class="tiles">
  <a class="tile tile-granite" href="#" role="img" aria-label="Grey granite mosaic wall with a plant">
    <span class="tile-label">GRANITE</span>
    <svg width="20" height="20" viewBox="0 0 20 20"><circle cx="10" cy="10" r="9" fill="none" stroke="#fff" stroke-width="1.6"/><path d="M5 10h9M10.5 6l4 4-4 4" fill="none" stroke="#fff" stroke-width="1.8"/></svg>
  </a>
  <a class="tile tile-marble" href="#" role="img" aria-label="Marble bathroom with washbasin and mosaic wall">
    <span class="tile-label">MARBLE</span>
    <svg width="20" height="20" viewBox="0 0 20 20"><circle cx="10" cy="10" r="9" fill="none" stroke="#fff" stroke-width="1.6"/><path d="M5 10h9M10.5 6l4 4-4 4" fill="none" stroke="#fff" stroke-width="1.8"/></svg>
  </a>
  <a class="tile tile-sculpture" href="#" role="img" aria-label="Two dark woven sculptures against a light wall">
    <span class="tile-label">SCULPTURE</span>
    <svg width="20" height="20" viewBox="0 0 20 20"><circle cx="10" cy="10" r="9" fill="none" stroke="#fff" stroke-width="1.6"/><path d="M5 10h9M10.5 6l4 4-4 4" fill="none" stroke="#fff" stroke-width="1.8"/></svg>
  </a>
</section>

<section class="welcome">
  <h2 class="section-title">Welcome to our website</h2>
  <p>Lorem ipsum dolor sit amet, consectetuer adipiscing elit. Praesent vestibulum molestie lacusLorem ipsum dolor sit amet, consectetuer adipiscing elit. Praesent vestibulum molestie lacusLorem ipsum dolor sit amet, consectetuer adipiscing elit. Praesent vestibulum molestie lacusLorem ipsum dolor sit amet, consectetuer adipiscing elit. Praesent vestibulum molestie lacusLorem ipsum dolor sit amet, consectetuer adipiscing elit.</p>
</section>
<div class="rule"></div>

<section class="projects"><h2 class="section-title">Recent projects</h2></section>
<div class="project-row">
  <article class="project"><div class="project-img" role="img" aria-label="Bathroom with white basins and dark mosaic" style="background:linear-gradient(135deg,#9a9a9a,#3c3c3c)"></div><h3>VESTIBULUM IACULIS</h3><p>Lacinia / Dictum</p></article>
  <article class="project"><div class="project-img" role="img" aria-label="Exterior wall clad in grey mosaic" style="background:linear-gradient(135deg,#7a6e62,#b8b2aa)"></div><h3>VESTIBULUM IACULIS</h3><p>Lacinia / Dictum</p></article>
  <article class="project"><div class="project-img" role="img" aria-label="Fireplace set in a bronze mosaic wall" style="background:linear-gradient(135deg,#3a2e28,#a0602a 55%,#4a3e36)"></div><h3>VESTIBULUM IACULIS</h3><p>Lacinia / Dictum</p></article>
  <article class="project"><div class="project-img" role="img" aria-label="Two dark woven sculptures on a sideboard" style="background:linear-gradient(135deg,#e4ddd8,#6a5550 55%,#e0d8d2)"></div><h3>VESTIBULUM IACULIS</h3><p>Lacinia / Dictum</p></article>
  <article class="project"><div class="project-img" role="img" aria-label="Patterned mosaic wall beside a bright window" style="background:linear-gradient(90deg,#5a5a5a,#d8d8d8 70%,#eee)"></div><h3>VESTIBULUM IACULIS</h3><p>Lacinia / Dictum</p></article>
</div>
<div class="dots"><span class="active"></span><span></span><span></span><span></span><span></span></div>

<footer class="footer">
  <div class="social"><span></span><span></span><span></span><span></span></div>
  <nav class="footer-nav"><a href="#">Home</a><a href="#">Collections</a><a href="#">Projects</a><a href="#">Installations</a><a href="#">About us</a><a href="#">Contact us</a></nav>
  <div class="legal">Terms &amp; Conditions &nbsp;|&nbsp; Privacy Policy</div>
</footer>
<div class="base">All rights reserved, copyrigths @ 2014</div>

</body>
</html>
```